We would like to incorporate our logo into letterhead design and envelopes. We are looking for something that is moderately conservative but not old law firm style. Both the envelopes and the letterhead must have both firm addresses. We would like to incorporate the color of the logo, but only a small amount of color - perhaps on one of the borders. The addresses for the firm locations are listed below. Given that it is a law firm, it needs to somewhat conservative, but not the old school, small black font on cream colored paper design.

The firm addresses are:

27815 N. Harlow Pemberton Pkwy.
Ste 4200
Scottsdale, AZ 85391

6100 W. Cedar Avenue
Ste 700
Burbank, CA 91623

Industry/Entity Type

Legal

Colors

Designer to choose colors to be used in the design.

Requirements
Must have
• Both addresses:
• 27815 N. Harlow Pemberton Pkwy.
• Ste 4200
• Scottsdale, AZ 85391
• 6100 W. Cedar Avenue
• Ste 700
• Burbank, CA 91623
Nice to have
• Small amount of color on border(s) that matches the logo but not too much color

```html
<!DOCTYPE html>
<html lang="en">
<head>
<meta charset="utf-8">
<title>Meridale Law Letterhead</title>
<link rel="stylesheet" href="https://fonts.googleapis.com/css2?family=Marcellus&family=Questrial&family=Open+Sans:wght@600&family=Tinos:wght@700&display=swap">
<style>
  :root {
    --backdrop: #d5def0;
    --paper: #ffffff;
    --accent: #66608f;
    --navy: #22205a;
    --ink: #2b2b2b;
    --muted: #555555;
  }
  * { box-sizing: border-box; margin: 0; padding: 0; }
  html, body { width: 1200px; height: 898px; overflow: hidden; background: var(--backdrop); }
  .canvas { position: relative; width: 1200px; height: 898px; }
  .letterhead {
    position: absolute; left: 275px; top: 29px; width: 650px; height: 840px;
    background: var(--paper); box-shadow: 0 6px 22px rgba(40, 50, 90, 0.18); overflow: hidden;
  }
  .letterhead__border { position: absolute; inset: 0; width: 650px; height: 840px; }
  .masthead { position: absolute; left: 50px; top: 108px; width: 520px; }
  .masthead__name {
    font-family: "Marcellus", serif; font-weight: 400; font-size: 40px; color: var(--navy);
    letter-spacing: 1px; text-align: center; line-height: 1;
  }
  .masthead__rule { height: 4px; background: var(--accent); margin: 10px 0 8px; }
  .contact {
    display: flex; justify-content: space-between; align-items: center;
    font-family: "Open Sans", sans-serif; font-weight: 600; font-size: 12px; color: #111;
  }
  .contact__item { display: flex; align-items: center; gap: 5px; white-space: nowrap; }
  .contact__icon { width: 12px; height: 12px; fill: #111; }
  .letter-body {
    position: absolute; left: 60px; top: 268px; width: 510px;
    font-family: "Questrial", sans-serif; font-size: 14px; line-height: 1.62; color: var(--ink);
  }
  .letter-body p + p { margin-top: 18px; }
  .signature { position: absolute; left: 470px; top: 620px; font-family: "Questrial", sans-serif; }
  .signature__name { font-size: 19px; color: #333; line-height: 1.2; }
  .signature__title { font-size: 12px; color: var(--muted); margin-top: 4px; }
  .offices {
    position: absolute; right: 30px; top: 716px; text-align: right;
    font-family: "Tinos", serif; font-weight: 700; font-size: 12.5px; color: #111; line-height: 1.5;
    white-space: nowrap;
  }
  .offices__rule { height: 3px; background: var(--navy); margin: 3px 0; width: 430px; margin-left: auto; }
</style>
</head>
<body>
<main class="canvas">
  <article class="letterhead">
    <svg class="letterhead__border" viewBox="0 0 650 840" aria-hidden="true">
      <path fill="var(--accent)" d="M190,0 H650 V235 C590,110 470,45 320,40 C260,38 215,25 190,0 Z"/>
      <path fill="var(--accent)" d="M0,690 C90,790 260,835 480,840 H0 Z"/>
    </svg>

    <header class="masthead">
      <h1 class="masthead__name">MERIDALE LAW</h1>
      <div class="masthead__rule"></div>
      <div class="contact">
        <span class="contact__item">
          <svg class="contact__icon" viewBox="0 0 24 24"><path d="M6.6 10.8a15 15 0 0 0 6.6 6.6l2.2-2.2c.3-.3.7-.4 1-.2 1.1.4 2.3.6 3.6.6.6 0 1 .4 1 1V20c0 .6-.4 1-1 1A17 17 0 0 1 3 4c0-.6.4-1 1-1h3.5c.6 0 1 .4 1 1 0 1.3.2 2.5.6 3.6.1.3 0 .7-.2 1z"/></svg>
          (855) 210-7736
        </span>
        <span class="contact__item">
          <svg class="contact__icon" viewBox="0 0 24 24"><path d="M2 5h20v14H2z M3 6l9 7 9-7" fill="none" stroke="#111" stroke-width="2"/></svg>
          info@northvalelegal.com
        </span>
        <span class="contact__item">
          <svg class="contact__icon" viewBox="0 0 24 24"><circle cx="12" cy="12" r="9" fill="none" stroke="#111" stroke-width="2"/><path d="M3 12h18M12 3c3 3 3 15 0 18M12 3c-3 3-3 15 0 18" fill="none" stroke="#111" stroke-width="1.6"/></svg>
          www.northvalelegal.com
        </span>
      </div>
    </header>

    <section class="letter-body">
      <p>Lorem ipsum dolor sit amet, consectetur adipiscing elit. Donec orci purus, luctus vitae dignissim eu, iaculis sed purus. Vivamus faucibus, ipsum nec aliquet viverra, leo mauris condimentum ligula, sit amet sagittis enim ligula quis arcu. Nam egestas tortor id nisi porttitor mattis. In tortor ante, ultricies in suscipit a, tempus non massa. Vivamus et auctor mi. Fusce vel massa nulla. Phasellus nec eros mauris, et scelerisque orci. Donec malesuada orci vitae nulla accumsan porta a id massa.</p>
      <p>Quisque accumsan iaculis magna sit amet fringilla. Maecenas consequat, magna eget tincidunt semper, odio nibh rutrum mi, id feugiat ante nisi eu risus. Vestibulum nunc orci, rhoncus a placerat in, ultricies in mi. Cras mattis varius eros, vel fringilla nisi suscipit eget. Quisque scelerisque sagittis nulla at porttitor. Mauris a justo et tellus interdum tristique. Sed id augue vitae urna euismod commodo aliquet a quam. Pellentesque arcu velit, cursus et malesuada ut, consequat et diam. Nullam erat sem, rhoncus id ullamcorper vitae, rhoncus et arcu. In ultricies ultricies nulla.</p>
    </section>

    <div class="signature">
      <p class="signature__name">Owen Reyes</p>
      <p class="signature__title">Co-Founder &amp; CEO</p>
    </div>

    <footer class="offices">
      <p>6100 W. Cedar Avenue, Ste 700, Burbank, CA 91623</p>
      <div class="offices__rule"></div>
      <p>27815 N. Harlow Pemberton Pkwy., Ste 4200, Scottsdale, AZ 85391</p>
    </footer>
  </article>
</main>
</body>
</html>
```